Velra Orchards Business Cards

design business cards for our new business should match my Copperline Quotes business cards

Contact Information for Business Card

2817 N 48th W Ave
Harlow Springs, KS 67012

Requirements
Must have
• should match logo colors

```html
<!DOCTYPE html>
<html lang="en">
<head>
<meta charset="utf-8">
<title>Velra Orchards Business Cards</title>
<link href="https://fonts.googleapis.com/css2?family=Michroma&family=Orbitron:wght@600;800&display=swap" rel="stylesheet">
<style>
  :root {
    --ink: #0a2b33;
    --green: #7ac143;
    --teal: #0aaab4;
    --paper: #ffffff;
    --stage: #e9ebea;
  }
  * { box-sizing: border-box; margin: 0; padding: 0; }
  html, body { width: 960px; height: 1200px; overflow: hidden; }
  body {
    background: var(--stage);
    display: flex;
    flex-direction: column;
    align-items: center;
    justify-content: space-evenly;
  }
  .card {
    position: relative;
    width: 800px;
    height: 457px;
    overflow: hidden;
    box-shadow: 0 6px 18px rgba(0,0,0,0.18);
  }
  .card--front { background: var(--ink); }
  .card--back { background: var(--paper); }

  .wordmark {
    position: absolute;
    display: flex;
    flex-direction: column;
    align-items: center;
    font-family: "Michroma", sans-serif;
    font-weight: 400;
  }
  .wordmark__dot {
    width: 26px; height: 26px;
    border-radius: 50%;
    margin-bottom: 14px;
  }
  .wordmark__top { font-size: 74px; letter-spacing: 4px; line-height: 1; }
  .wordmark__bottom { font-size: 30px; letter-spacing: 16px; margin-top: 16px; margin-right: -16px; }

  .card--front .wordmark {
    left: 0; right: 0; top: 120px;
    color: var(--green);
  }
  .card--front .wordmark__dot { background: var(--green); }

  .card--back .wordmark {
    left: 30px; width: 380px; top: 130px;
    color: var(--ink);
  }
  .card--back .wordmark__dot { background: var(--ink); }
  .card--back .wordmark__top { font-size: 54px; }
  .card--back .wordmark__bottom { font-size: 21px; letter-spacing: 11px; margin-right: -11px; }

  .bands { position: absolute; inset: 0; }

  .person {
    position: absolute;
    left: 460px; top: 112px;
    width: 310px;
    text-align: center;
  }
  .person__name {
    font-family: "Orbitron", sans-serif;
    font-weight: 800;
    font-size: 30px;
    letter-spacing: 1px;
    color: var(--green);
  }
  .person__role {
    font-family: "Michroma", sans-serif;
    font-size: 9px;
    letter-spacing: 9px;
    color: var(--teal);
    margin-top: 4px;
  }

  .contact {
    position: absolute;
    left: 465px; top: 250px;
    width: 320px;
    list-style: none;
    font-family: "Orbitron", sans-serif;
    font-weight: 600;
    font-size: 13px;
    color: var(--ink);
    letter-spacing: 0.5px;
  }
  .contact__item {
    display: flex;
    align-items: flex-start;
    gap: 16px;
    margin-bottom: 16px;
    line-height: 1.35;
  }
  .contact__icon { width: 18px; height: 18px; flex: none; }
</style>
</head>
<body>

  <section class="card card--front" aria-label="Business card front">
    <div class="wordmark">
      <span class="wordmark__dot"></span>
      <span class="wordmark__top">VELRA</span>
      <span class="wordmark__bottom">ORCHARDS</span>
    </div>
  </section>

  <section class="card card--back" aria-label="Business card back">
    <svg class="bands" width="800" height="457" viewBox="0 0 800 457" aria-hidden="true">
      <polygon points="430,0 800,0 800,48 395,48" fill="var(--teal)"/>
      <polygon points="0,405 360,405 395,457 0,457" fill="var(--green)"/>
    </svg>

    <div class="wordmark">
      <span class="wordmark__dot"></span>
      <span class="wordmark__top">VELRA</span>
      <span class="wordmark__bottom">ORCHARDS</span>
    </div>

    <div class="person">
      <p class="person__name">DENA MARLOW</p>
      <p class="person__role">PRESIDENT</p>
    </div>

    <ul class="contact">
      <li class="contact__item">
        <svg class="contact__icon" viewBox="0 0 18 18" aria-hidden="true">
          <rect x="5" y="1" width="8" height="16" rx="1.5" fill="none" stroke="var(--teal)" stroke-width="1.6"/>
          <circle cx="9" cy="14" r="1" fill="var(--teal)"/>
        </svg>
        <span>918-555-0147</span>
      </li>
      <li class="contact__item">
        <svg class="contact__icon" viewBox="0 0 18 18" aria-hidden="true">
          <rect x="1" y="4" width="16" height="11" fill="none" stroke="var(--teal)" stroke-width="1.4"/>
          <polyline points="1,4 9,11 17,4" fill="none" stroke="var(--teal)" stroke-width="1.4"/>
        </svg>
        <span>DMARLOW@VELRAORCHARDS.COM</span>
      </li>
      <li class="contact__item">
        <svg class="contact__icon" viewBox="0 0 18 18" aria-hidden="true">
          <circle cx="9" cy="9" r="7.5" fill="none" stroke="var(--teal)" stroke-width="1.4"/>
          <ellipse cx="9" cy="9" rx="3.2" ry="7.5" fill="none" stroke="var(--teal)" stroke-width="1.2"/>
          <line x1="1.5" y1="9" x2="16.5" y2="9" stroke="var(--teal)" stroke-width="1.2"/>
          <line x1="3" y1="5" x2="15" y2="5" stroke="var(--teal)" stroke-width="1"/>
          <line x1="3" y1="13" x2="15" y2="13" stroke="var(--teal)" stroke-width="1"/>
        </svg>
        <span>WWW.VELRAORCHARDS.COM</span>
      </li>
      <li class="contact__item">
        <svg class="contact__icon" viewBox="0 0 18 18" aria-hidden="true">
          <path d="M9 1a6 6 0 0 0-6 6c0 4.5 6 10 6 10s6-5.5 6-10a6 6 0 0 0-6-6z" fill="var(--teal)"/>
          <circle cx="9" cy="7" r="2.2" fill="var(--paper)"/>
        </svg>
        <span>2817 N 48TH W AVE<br>HARLOW SPRINGS, KS 67012</span>
      </li>
    </ul>
  </section>

</body>
</html>
```